Marnie Vale Photography needs a unique, creative business card/logo design

I need a design for business cards/logo that is unique and creative in the industry. Simplicity is nice, so not too crowded. Something that will catch my customer's eye and remain in their memory. I am primarily a landscape photographer but will be soon may be branching into boudoir photography as well. I have attached my current card.

Marnie Vale Photography
Phone: 0439 517 264
Email: MarnieValePhotography@quillmail.example
Website: www.snapnook.example/MarnieValePhotography.Aust

Marnie Vale Photography

• Contact Details on one side
• pixelation

```html
<!DOCTYPE html>
<html lang="en">
<head>
<meta charset="utf-8">
<title>Marnie Vale Photography – Business Card</title>
<link rel="stylesheet" href="https://fonts.googleapis.com/css2?family=Josefin+Sans:wght@300;400;600;700&display=swap">
<style>
  :root {
    --canvas-bg: #ecebe8;
    --card-white: #ffffff;
    --brand-aqua: #a8ddd6;
    --ink: #141414;
    --card-shadow: rgba(0, 0, 0, 0.12);
  }
  html, body {
    margin: 0;
    padding: 0;
    width: 1200px;
    height: 900px;
    overflow: hidden;
    background: var(--canvas-bg);
  }
  .canvas {
    position: relative;
    width: 1200px;
    height: 900px;
  }
  .card {
    position: absolute;
    left: 325px;
    width: 550px;
    height: 320px;
    background: var(--card-white);
    box-shadow: 0 6px 22px var(--card-shadow);
    box-sizing: border-box;
  }
  .card--front { top: 95px; }
  .card--back { top: 480px; padding: 42px 32px 0 32px; }

  /* Front: brand */
  .brand {
    display: flex;
    flex-direction: column;
    align-items: center;
    padding-top: 62px;
  }
  .brand__dot {
    width: 58px;
    height: 58px;
    border-radius: 50%;
    background: var(--brand-aqua);
    margin-bottom: 14px;
  }
  .brand__name {
    margin: 0;
    font-family: "Josefin Sans", sans-serif;
    font-weight: 400;
    color: var(--brand-aqua);
    text-transform: uppercase;
    text-align: center;
    line-height: 1.05;
    font-size: 40px;
    letter-spacing: 0.09em;
  }
  .brand__line { display: block; }

  /* Back: contact */
  .contact {
    font-family: "Josefin Sans", sans-serif;
    color: var(--ink);
  }
  .contact__name {
    margin: 0;
    font-size: 25px;
    font-weight: 700;
    font-variant: small-caps;
    letter-spacing: 0.05em;
  }
  .contact__role {
    margin: 2px 0 0 0;
    font-size: 16px;
    font-weight: 400;
    letter-spacing: 0.03em;
  }
  .contact__list {
    list-style: none;
    margin: 48px 0 0 0;
    padding: 0;
    font-size: 15.5px;
    font-weight: 400;
    font-variant: small-caps;
    letter-spacing: 0.03em;
    line-height: 1.55;
    white-space: nowrap;
  }
</style>
</head>
<body>
  <main class="canvas">
    <section class="card card--front" aria-label="Card front">
      <div class="brand">
        <span class="brand__dot" aria-hidden="true"></span>
        <h1 class="brand__name">
          <span class="brand__line">Marnie Vale</span>
          <span class="brand__line">Photography</span>
        </h1>
      </div>
    </section>

    <section class="card card--back contact" aria-label="Card back">
      <h2 class="contact__name">Marnie Vale</h2>
      <p class="contact__role">Photographer</p>
      <ul class="contact__list">
        <li>Phone: 0439 517 264</li>
        <li>Email: MarnieValePhotography@quillmail.example</li>
        <li>Website: www.snapnook.example/MarnieValePhotography.Aust</li>
      </ul>
    </section>
  </main>
</body>
</html>
```